Q-Rolls Business Card

We are a modern retail clothing store. Established in 1994. I need a presentable card that will amaze vendors when given to them.

Front: Logo in middle
Info Side:

Name: Tomas Velder
Cell: 630-812-4463
Work: 630-917-3384 EXT. 417
Email: Tomas@q-rolls-example.com
Website: www.Q-rolls-example.com

Industry/Entity Type

Business

```html
<!DOCTYPE html>
<html lang="en">
<head>
<meta charset="utf-8">
<title>Q-Rolls Business Card</title>
<link href="https://fonts.googleapis.com/css2?family=Saira:wght@500;600;700&display=swap" rel="stylesheet">
<style>
  :root {
    --backdrop: #d9d9d9;
    --card: #000000;
    --ink-white: #ffffff;
    --ink-label: #c9c9c9;
    --ink-value: #8f8f8f;
  }
  * { box-sizing: border-box; margin: 0; padding: 0; }
  html, body {
    width: 1200px;
    height: 903px;
    overflow: hidden;
    background: var(--backdrop);
    font-family: "Saira", sans-serif;
  }
  .stage {
    width: 1200px;
    height: 903px;
    display: flex;
    align-items: center;
    justify-content: center;
    gap: 60px;
  }
  .card {
    width: 525px;
    height: 300px;
    background: var(--card);
    position: relative;
    box-shadow: 0 10px 24px rgba(0,0,0,0.25);
  }
  .card-front {
    display: flex;
    align-items: center;
    justify-content: center;
  }
  .brand-name {
    color: var(--ink-white);
    font-weight: 700;
    font-size: 64px;
    letter-spacing: 3px;
    text-transform: uppercase;
  }
  .card-info {
    padding: 62px 0 0;
  }
  .holder-name {
    color: var(--ink-white);
    font-weight: 600;
    font-size: 20px;
    letter-spacing: 1.5px;
    text-align: center;
  }
  .contact-list {
    position: absolute;
    left: 0;
    right: 0;
    bottom: 46px;
    display: grid;
    grid-template-columns: auto auto;
    justify-content: center;
    column-gap: 6px;
    row-gap: 2px;
    font-size: 14px;
    letter-spacing: 0.8px;
  }
  .contact-label {
    color: var(--ink-label);
    font-weight: 600;
    text-align: right;
  }
  .contact-value {
    color: var(--ink-value);
    font-weight: 500;
  }
</style>
</head>
<body>
  <main class="stage">
    <section class="card card-front" aria-label="Card front">
      <span class="brand-name">Q-Rolls</span>
    </section>
    <section class="card card-info" aria-label="Card back">
      <p class="holder-name">Tomas Velder</p>
      <dl class="contact-list">
        <dt class="contact-label">Cell:</dt>
        <dd class="contact-value">630-812-4463</dd>
        <dt class="contact-label">Work:</dt>
        <dd class="contact-value">630-917-3384 EXT. 417</dd>
        <dt class="contact-label">Email:</dt>
        <dd class="contact-value">Tomas@q-rolls-example.com</dd>
        <dt class="contact-label">Website:</dt>
        <dd class="contact-value">www.Q-rolls-example.com</dd>
      </dl>
    </section>
  </main>
</body>
</html>
```